Business card design for QuelMarvion

I need a business card based on the logo design produced for QuelMarvion. The company is focused on triathlon and endurance sport coaching and the tag line is (per the logo) "Endurance. Resilience. Achievement". The design should be sophisticated, appropriate to an affluent and business oriented target market. Colors are optional but the color of the logo probably dictates the color used on the card. I envisage using the red logo, with black print for the wording and contact numbers on a white or cream background, but am open to alternative suggestions. I expect to select something fairly conventional, but would like to see some designs that are less conventional to stretch my thinking on what could be appropriate. I am assuming a single side design is best, but willing to consider double sided as an option.

Target Market(s)

Individual athletes and corporate health and wellness leaders

Industry/Entity Type

Health And Wellness

Contact Information for Business Card

The card should provide the following information:
Logo
My name: Gordon Lashby
Company website: QuelMarvion.com
My email: gordon.lashby@quelmarvion.com
My cell phone number: +1-555-018-2739

Font styles to use
Sans Serif

Colors

Designer to choose colors to be used in the design.

Requirements
Must have
• Space on the card - simple design, not over crowded.
Nice to have
• clean and clear font, nothing garish or mass market like
Should not have
• Do not add pictures

```html
<!DOCTYPE html>
<html lang="en">
<head>
<meta charset="utf-8">
<title>QuelMarvion Business Card</title>
<link rel="stylesheet" href="https://fonts.googleapis.com/css2?family=Lato:wght@400;700&display=swap">
<style>
  :root {
    --brand-red: #b0262a;
    --ink: #141414;
    --paper: #ffffff;
    --backdrop: #e9e6e1;
  }
  * { margin: 0; padding: 0; box-sizing: border-box; }
  html, body {
    width: 1200px;
    height: 902px;
    overflow: hidden;
    background: var(--backdrop);
    font-family: "Lato", Arial, sans-serif;
  }
  .card {
    position: absolute;
    left: 80px;
    top: 154px;
    width: 1040px;
    height: 593px;
    background: var(--paper);
    box-shadow: 0 6px 24px rgba(0,0,0,0.12);
    overflow: hidden;
  }
  .brand {
    position: absolute;
    right: 61px;
    top: 112px;
    text-align: right;
  }
  .brand-name {
    display: block;
    font-size: 60px;
    font-weight: 700;
    line-height: 1;
    color: var(--brand-red);
    letter-spacing: 0.5px;
  }
  .holder-name {
    position: absolute;
    left: 46px;
    top: 364px;
    font-size: 31px;
    font-weight: 700;
    color: var(--brand-red);
    line-height: 1.1;
  }
  .name-rule {
    position: absolute;
    left: 46px;
    top: 409px;
    width: 941px;
    height: 2px;
    background: var(--ink);
  }
  .contact-band {
    position: absolute;
    left: 0;
    top: 459px;
    width: 100%;
    height: 101px;
    background: var(--brand-red);
    display: flex;
    align-items: center;
    padding-left: 46px;
    color: var(--paper);
    font-size: 24px;
    font-weight: 400;
  }
  .contact-item { white-space: nowrap; }
  .contact-divider {
    width: 2px;
    height: 54px;
    background: var(--paper);
    margin: 0 16px;
  }
  .base-band {
    position: absolute;
    left: 0;
    bottom: 0;
    width: 100%;
    height: 28px;
    background: var(--ink);
  }
</style>
</head>
<body>
  <section class="card">
    <div class="brand">
      <span class="brand-name">QuelMarvion</span>
    </div>

    <h1 class="holder-name">Gordon Lashby</h1>
    <div class="name-rule"></div>

    <div class="contact-band">
      <span class="contact-item phone">+1-555-018-2739</span>
      <span class="contact-divider"></span>
      <span class="contact-item email">gordon.lashby@quelmarvion.com</span>
      <span class="contact-divider"></span>
      <span class="contact-item website">QuelMarvion.com</span>
    </div>

    <div class="base-band"></div>
  </section>
</body>
</html>
```